Infographic for Commercial Painting and Flooring Company

We need an Infographic that shows a compelling argument for signing on with Verimbos for a maintenance contract vs a project. The infographic should be easily understood visually so sell the story we have provided. 1) What does the quick view give me? 2) Am I interested in this? 3) Does this bring me any value? 4) Is this “everything I have seen before or something new and different”? Included here is a word document called Maintenance vs Project Notes with the written content and instructions, a logo, and two other marketing pieces they currently use so you can see how their brand is being used. Colors should be on brand. I'd like to get this done ASAP if possible. We do not want this piece to look busy.

I added two images called Sample 1 and Sample 2 to portray the types of infographics we like. Simple and clear. Love the watch with the pie chart built in....a smaller version of that would be great for us based on the notes document I provided.

Target Market(s)

Facilities Manufacturers and owners of manufacturing facilities

Font styles to use
Sans Serif

Colors

Designer to choose colors to be used in the design.

Requirements
Must have
• Simple, clean, tell a clear story
Nice to have
• Iconography, pie chart, Men in hard hat
Should not have
• Too many colors. Stick with the brand colors and maybe a few others. Don't want it too look to busy.

```html
<!DOCTYPE html>
<html lang="en">
<head>
<meta charset="utf-8">
<title>Verimbos – Maintenance Contract vs a Project</title>
<link rel="stylesheet" href="https://fonts.googleapis.com/css2?family=Oswald:wght@300;400;500;600&family=Montserrat:wght@700;800&family=Nunito+Sans:wght@400;600&display=swap">
<style>
  :root{
    --navy:#143c73;
    --navy-deep:#0f2f5e;
    --blue-tail:#1e57a3;
    --olive:#8e8b1f;
    --olive-bright:#a39d22;
    --olive-ribbon:#b3ab2b;
    --olive-tail:#8a8420;
    --grey-band:#e3e3e3;
    --ink:#333333;
    --ink-soft:#555555;
    --white:#ffffff;
  }
  html,body{margin:0;padding:0;overflow:hidden;background:var(--white);}
  .canvas{position:relative;width:1200px;height:3168px;overflow:hidden;background:var(--white);font-family:"Nunito Sans",sans-serif;color:var(--ink);}
  .abs{position:absolute;}
  .band-olive{left:0;top:397px;width:1200px;height:255px;background:var(--olive);}
  .band-grey{left:0;top:802px;width:1200px;height:77px;background:var(--grey-band);}
  .band-stats{left:0;top:1704px;width:1200px;height:125px;background:var(--grey-band);}
  .band-navy{left:0;top:1840px;width:1200px;height:1308px;background:var(--navy);}
  .band-footer{left:0;top:3148px;width:1200px;height:20px;background:var(--olive);}
  .graphics{left:0;top:0;width:1200px;height:3168px;}
  .brand{left:0;top:120px;width:1200px;display:flex;justify-content:center;align-items:center;gap:26px;}
  .brand-mark{width:70px;height:70px;border-radius:50%;background:var(--olive);}
  .brand-name{font-family:"Montserrat",sans-serif;font-weight:800;font-size:96px;color:var(--navy);letter-spacing:-1px;line-height:1;}
  .ribbon-text{font-family:"Montserrat",sans-serif;font-weight:800;color:var(--white);text-align:center;white-space:nowrap;}
  .ribbon-title{left:216px;top:273px;width:765px;height:65px;line-height:65px;font-size:33.5px;}
  .ribbon-hours{left:391px;top:931px;width:416px;height:80px;line-height:80px;font-size:33px;}
  .ribbon-solution{left:391px;top:1875px;width:416px;height:80px;line-height:80px;font-size:33px;}
  .imagine{left:99px;top:452px;font-family:"Oswald",sans-serif;color:var(--white);text-transform:uppercase;white-space:nowrap;z-index:2;}
  .imagine-line1{font-weight:300;font-size:57px;line-height:70px;letter-spacing:-0.5px;}
  .imagine-line2{font-weight:400;font-size:43px;line-height:76px;}
  .imagine-line2 .big{font-size:76px;font-weight:500;}
  .illustration{left:815px;top:389px;width:385px;height:490px;background:linear-gradient(160deg,#f4f4f4 0%,#d9d9d9 40%,#6b6b6b 70%,#1f1f1f 100%);}
  .intro{left:82px;top:676px;width:580px;font-size:27px;line-height:34px;color:var(--ink);margin:0;}
  .source-heading{left:0;top:1026px;width:1200px;text-align:center;font-family:"Oswald",sans-serif;font-weight:500;font-size:42px;line-height:60px;color:var(--olive-bright);text-transform:uppercase;white-space:nowrap;}
  .stats{left:132px;top:1720px;font-size:29px;line-height:47px;color:var(--ink);white-space:nowrap;}
  .stats p{margin:0;}
  .program-heading{left:0;top:1968px;width:1200px;text-align:center;font-family:"Oswald",sans-serif;font-weight:500;font-size:42px;line-height:60px;color:var(--white);text-transform:uppercase;}
  .pill{background:var(--white);border-radius:40px;font-family:"Montserrat",sans-serif;font-weight:800;color:var(--olive-bright);text-align:center;white-space:nowrap;}
  .pill-time{left:296px;top:2066px;width:608px;height:64px;line-height:64px;font-size:33px;}
  .pill-partner{left:86px;top:2484px;width:1028px;height:62px;line-height:62px;font-size:33px;}
  .benefit{color:var(--white);font-size:27.5px;line-height:34px;white-space:nowrap;}
  .benefit-comm{left:298px;top:2184px;}
  .benefit-safety{left:406px;top:2274px;}
  .benefit-prod{left:203px;top:2361px;}
  .partner-table{left:79px;top:2567px;width:1042px;height:541px;border:2px solid var(--white);box-sizing:border-box;}
  .partner-divider{left:415px;top:2567px;width:2px;height:541px;background:var(--white);}
  .quality{left:101px;display:flex;align-items:center;gap:16px;font-family:"Montserrat",sans-serif;font-weight:800;font-size:28.5px;color:var(--white);line-height:40px;white-space:nowrap;}
  .quality svg{width:28px;height:28px;}
  .feature-list{margin:0;padding:0;list-style:none;}
  .feature{position:absolute;left:440px;width:660px;color:var(--white);font-size:27px;line-height:31px;padding-left:36px;}
  .feature::before{content:"";position:absolute;left:0;top:10px;width:11px;height:11px;border-radius:50%;background:var(--white);}
</style>
</head>
<body>
<div class="canvas">
  <div class="abs band-olive"></div>
  <div class="abs band-grey"></div>
  <div class="abs band-stats"></div>
  <div class="abs band-navy"></div>
  <div class="abs band-footer"></div>

  <svg class="abs graphics" viewBox="0 0 976 2576" preserveAspectRatio="none" aria-hidden="true">
    <g fill="var(--olive)">
      <rect x="64" y="0" width="16" height="275"/>
      <rect x="64" y="259" width="60" height="16"/>
      <polygon points="110,245 134,267 110,289 124,289 148,267 124,245"/>
      <rect x="896" y="0" width="16" height="275"/>
      <rect x="852" y="259" width="60" height="16"/>
      <polygon points="866,245 842,267 866,289 852,289 828,267 852,245"/>
    </g>
    <polygon fill="var(--blue-tail)" points="112,241 205,241 205,292 112,292 140,266"/>
    <polygon fill="var(--blue-tail)" points="864,241 771,241 771,292 864,292 836,266"/>
    <polygon fill="var(--navy-deep)" points="176,275 205,292 205,275"/>
    <polygon fill="var(--navy-deep)" points="798,275 771,292 771,275"/>
    <rect x="176" y="222" width="622" height="53" fill="var(--navy)"/>
    <rect x="64" y="361" width="848" height="135" fill="none" stroke="var(--white)" stroke-width="3"/>

    <polygon fill="var(--blue-tail)" points="260,778 345,778 345,823 260,823 290,800"/>
    <polygon fill="var(--blue-tail)" points="716,778 630,778 630,823 716,823 686,800"/>
    <polygon fill="var(--navy-deep)" points="318,822 345,823 345,810"/>
    <polygon fill="var(--navy-deep)" points="656,822 630,823 630,810"/>
    <rect x="318" y="757" width="338" height="65" fill="var(--navy)"/>

    <g fill="none" stroke="var(--olive)" stroke-width="1.6">
      <polyline points="104,975 104,919 572,919"/>
      <polyline points="234,936 540,936 540,973 572,973"/>
      <polyline points="424,956 522,956 522,1027 572,1027"/>
      <polyline points="525,1081 572,1081"/>
      <polyline points="416,1200 512,1200 512,1135 572,1135"/>
      <polyline points="228,1217 228,1232 534,1232 534,1189 572,1189"/>
      <polyline points="100,1172 100,1265 572,1265"/>
      <polyline points="62,1128 62,1341 572,1341"/>
    </g>

    <g class="pie-chart" transform="translate(43.9,926.8) scale(0.813)">
      <g stroke="#1c2f4d" stroke-width="1">
        <path fill="#294a78" d="M580,130 A280,110 0 0,1 508.1,203.6 L508.1,263.6 A280,110 0 0,0 580,190 Z"/>
        <path fill="#1f3556" d="M508.1,203.6 A280,110 0 0,1 358.2,237.6 L358.2,297.6 A280,110 0 0,0 508.1,263.6 Z"/>
        <path fill="#3a5f96" d="M358.2,237.6 A280,110 0 0,1 135.4,219 L135.4,279 A280,110 0 0,0 358.2,297.6 Z"/>
        <path fill="#4a6ca3" d="M135.4,219 A280,110 0 0,1 57.5,185 L57.5,245 A280,110 0 0,0 135.4,279 Z"/>
        <path fill="#6f88b8" d="M57.5,185 A280,110 0 0,1 20,130 L20,190 A280,110 0 0,0 57.5,245 Z"/>
      </g>
      <g stroke="#23395c" stroke-width="1.5">
        <path fill="#2e5283" d="M300,130 L300,20 A280,110 0 0,1 508.1,56.4 Z"/>
        <path fill="#3a6197" d="M300,130 L508.1,56.4 A280,110 0 0,1 508.1,203.6 Z"/>
        <path fill="#2f5688" d="M300,130 L508.1,203.6 A280,110 0 0,1 358.2,237.6 Z"/>
        <path fill="#4a75b0" d="M300,130 L358.2,237.6 A280,110 0 0,1 135.4,219 Z"/>
        <path fill="#5f83bb" d="M300,130 L135.4,219 A280,110 0 0,1 57.5,185 Z"/>
        <path fill="#8ea4cf" d="M300,130 L57.5,185 A280,110 0 0,1 33.7,96 Z"/>
        <path fill="#a5b5d7" d="M300,130 L33.7,96 A280,110 0 0,1 135.4,41 Z"/>
        <path fill="#c5cde3" d="M300,130 L135.4,41 A280,110 0 0,1 300,20 Z"/>
      </g>
      <g fill="var(--white)" font-family="Nunito Sans, sans-serif" font-size="18" text-anchor="middle">
        <text x="363" y="70">4 hours</text>
        <text x="482" y="142">7 hours</text>
        <text x="410" y="225">3 hours</text>
        <text x="257" y="236">4 hours</text>
        <text x="123" y="212">2 hours</text>
        <text x="103" y="144">4 hours</text>
        <text x="153" y="89">3 hours</text>
        <text x="252" y="62">3 hours</text>
      </g>
    </g>

    <g fill="var(--white)" stroke="var(--olive)" stroke-width="1.6">
      <circle cx="104" cy="975" r="4"/><circle cx="234" cy="936" r="4"/>
      <circle cx="424" cy="956" r="4"/><circle cx="525" cy="1081" r="4"/>
      <circle cx="416" cy="1200" r="4"/><circle cx="228" cy="1217" r="4"/>
      <circle cx="100" cy="1172" r="4"/><circle cx="62" cy="1128" r="4"/>
    </g>

    <g fill="var(--ink-soft)" font-family="Nunito Sans, sans-serif" font-size="19">
      <text x="585" y="925">Awarding &amp; Purchasing</text>
      <text x="585" y="979">Completing On-Boarding Paperwork</text>
      <text x="585" y="1033">Source Vendors &amp; Bidders</text>
      <text x="585" y="1087">Schedule &amp; Completing a Walkthrough</text>
      <text x="585" y="1141">Reviewing Estimates</text>
      <text x="585" y="1195">Phone calls to clarify scope &amp; any big</text>
      <text x="585" y="1217">revisions</text>
      <text x="585" y="1271">Present to Decision Maker &amp; Financing</text>
      <text x="585" y="1293">Approval</text>
      <text x="585" y="1347">Negotiations with Vendor</text>
    </g>

    <polygon fill="var(--olive-tail)" points="260,1546 345,1546 345,1591 260,1591 290,1568"/>
    <polygon fill="var(--olive-tail)" points="716,1546 630,1546 630,1591 716,1591 686,1568"/>
    <polygon fill="#6b6616" points="318,1590 345,1591 345,1578"/>
    <polygon fill="#6b6616" points="656,1590 630,1591 630,1578"/>
    <rect x="318" y="1525" width="338" height="65" fill="var(--olive-ribbon)"/>

    <g class="icon-phone">
      <circle cx="198" cy="1790" r="33" fill="var(--white)" stroke="var(--olive)" stroke-width="3"/>
      <path fill="var(--olive)" d="M178,1784 q20,-16 40,0 l0,6 l-9,0 l-2,-6 q-9,-3 -18,0 l-2,6 l-9,0 Z"/>
      <path fill="var(--olive)" d="M186,1791 l24,0 l5,15 l-34,0 Z"/>
      <g fill="var(--white)"><circle cx="193" cy="1797" r="1.5"/><circle cx="198" cy="1797" r="1.5"/><circle cx="203" cy="1797" r="1.5"/><circle cx="193" cy="1802" r="1.5"/><circle cx="198" cy="1802" r="1.5"/><circle cx="203" cy="1802" r="1.5"/></g>
    </g>
    <g class="icon-cone">
      <circle cx="285" cy="1863" r="33" fill="var(--white)" stroke="var(--olive)" stroke-width="3"/>
      <path fill="var(--olive)" d="M281,1841 l8,0 l10,30 l-28,0 Z"/>
      <rect x="268" y="1871" width="34" height="5" fill="var(--olive)"/>
      <rect x="276" y="1853" width="18" height="4" fill="var(--white)"/>
      <rect x="273" y="1862" width="24" height="4" fill="var(--white)"/>
    </g>
    <g class="icon-gears">
      <circle cx="120" cy="1934" r="33" fill="var(--white)" stroke="var(--olive)" stroke-width="3"/>
      <circle cx="112" cy="1926" r="10" fill="none" stroke="var(--olive)" stroke-width="6" stroke-dasharray="4 3"/>
      <circle cx="112" cy="1926" r="5" fill="var(--olive)"/>
      <circle cx="129" cy="1944" r="7" fill="none" stroke="var(--olive)" stroke-width="5" stroke-dasharray="3 2.5"/>
      <circle cx="118" cy="1952" r="4" fill="none" stroke="var(--olive)" stroke-width="3"/>
    </g>
  </svg>

  <div class="abs brand">
    <span class="brand-mark"></span>
    <span class="brand-name">Verimbos</span>
  </div>
  <div class="abs ribbon-text ribbon-title">MAINTENANCE CONTRACT v/s A PROJECT</div>

  <div class="abs illustration" role="img" aria-label="Illustration of a businessman in glasses typing on a laptop, with a thought bubble wondering what he can do"></div>

  <div class="abs imagine">
    <div class="imagine-line1">Imagine what you could do with</div>
    <div class="imagine-line2">An extra <span class="big">30%</span> more time each year?</div>
  </div>

  <p class="abs intro">Time that you wouldn’t need to spend on-<br>boarding a new company every time you<br>have a project or facility upgrade.</p>

  <div class="abs ribbon-text ribbon-hours">IT TAKES 30+ HOURS</div>
  <div class="abs source-heading">To source and onboard the most qualified vendor...yikes!</div>

  <div class="abs stats">
    <p>20 Projects = 600Hours or 25% of Your Time Per Year...UGGH!</p>
    <p>On-Boarding Once = 1.5 % of Your Time for the entire year....FOR REAL!</p>
  </div>

  <div class="abs ribbon-text ribbon-solution">A BETTER SOLUTION</div>
  <div class="abs program-heading">A Preventative Maintenance Program</div>

  <div class="abs pill pill-time">YOU’LL HAVE MORE TIME TO...</div>
  <div class="abs benefit benefit-comm">Focus on Communication with Your Team and Customers</div>
  <div class="abs benefit benefit-safety">Focus on Safety to ensure it is a priority</div>
  <div class="abs benefit benefit-prod">Focus on Productivity to ensure you meet all ofyour business unit’s needs</div>

  <div class="abs pill pill-partner">YOU’LL HAVE A TRUSTED PARTNER WHO PROVIDES...</div>

  <div class="abs partner-table"></div>
  <div class="abs partner-divider"></div>

  <div class="abs quality" style="top:2601px">
    <svg viewBox="0 0 28 28"><rect x="2" y="2" width="24" height="24" fill="none" stroke="#fff" stroke-width="3"/><polyline points="7,14 12,19 22,8" fill="none" stroke="#fff" stroke-width="3"/></svg>CONSISTENCY
  </div>
  <div class="abs quality" style="top:2667px">
    <svg viewBox="0 0 28 28"><rect x="2" y="2" width="24" height="24" fill="none" stroke="#fff" stroke-width="3"/><polyline points="7,14 12,19 22,8" fill="none" stroke="#fff" stroke-width="3"/></svg>PREDICTABILITY
  </div>
  <div class="abs quality" style="top:2733px">
    <svg viewBox="0 0 28 28"><rect x="2" y="2" width="24" height="24" fill="none" stroke="#fff" stroke-width="3"/><polyline points="7,14 12,19 22,8" fill="none" stroke="#fff" stroke-width="3"/></svg>RELIABILITY
  </div>

  <ul class="feature-list">
    <li class="feature" style="top:2605px">Safety Is Our #1 Objective</li>
    <li class="feature" style="top:2654px">Adapting to all ofYour Scheduling Requirements</li>
    <li class="feature" style="top:2702px">A Single Point of Communication</li>
    <li class="feature" style="top:2751px">Integration w/ your Work Order Process&amp;Project<br>Tracking</li>
    <li class="feature" style="top:2831px">A Dedicated Field Team,who Understands the<br>Ins and Outs of Your Facility</li>
    <li class="feature" style="top:2910px">Rapid Response Time</li>
    <li class="feature" style="top:2958px">All Tasks and Jobs (Big or Small) Equally Prioritized</li>
    <li class="feature" style="top:3007px">Customized Billing and Future Budget Building</li>
    <li class="feature" style="top:3055px">Visual Facility Mapping</li>
  </ul>
</div>
</body>
</html>
```